Used Car Dealer seeks an Amazing Business Card Design

We are looking for a business card design that incorporates our logo and grabs the attention of anyone we give the business card to.

Looking to use the same colors as the logo. Our Logo choice is the black background with Red and Silver/Grey Lettering.

We also would like to see some embossed designs.

Target Market(s)

Used Car Buyers, Automotive, Auto

Industry/Entity Type

Automotive

Contact Information for Business Card

BVEL7K
Gordon Whitlock
482 Tarrow Lane
Suite 207
Marlow Springs, GA 30412
Office (770) 555-0142
Cell (770) 555-0187
bvel7kga@quellmail.com
www.bvel7kga.com

Colors
ffffff
ee3036

Requirements
Must have
• Must include our logo (Black Background with Red and Silver/Grey Lettering)
Nice to have
• Embossed Design. Can be Single or Double Sided.

```html
<!DOCTYPE html>
<html lang="en">
<head>
<meta charset="utf-8">
<title>BVEL7K Business Card</title>
<link rel="stylesheet" href="https://fonts.googleapis.com/css2?family=Montserrat:wght@500;600;800&display=swap">
<style>
  :root {
    --card-black: #141414;
    --card-black-mid: #1e1e1e;
    --swoosh-white: #e9e9e9;
    --accent-red: #ee3036;
    --text-white: #ffffff;
    --silver: #c9c9c9;
    --page-bg: #3a3735;
  }
  * { box-sizing: border-box; margin: 0; padding: 0; }
  html, body {
    width: 1200px; height: 716px; overflow: hidden;
    background: var(--page-bg);
    font-family: "Montserrat", sans-serif;
  }
  .canvas {
    width: 1200px; height: 716px;
    display: flex; align-items: center; justify-content: center; gap: 40px;
  }
  .card {
    position: relative;
    width: 540px; height: 309px;
    overflow: hidden;
    box-shadow: 0 12px 30px rgba(0,0,0,.45);
  }
  .card-bg { position: absolute; inset: 0; width: 100%; height: 100%; }
  .brand {
    position: absolute;
    display: flex; align-items: center; gap: 12px;
    color: var(--silver);
    font-weight: 800;
    letter-spacing: 2px;
    white-space: nowrap;
  }
  .brand-dot {
    width: 16px; height: 16px; border-radius: 50%;
    background: var(--accent-red);
  }
  .card-front .brand { left: 50%; top: 50%; transform: translate(-50%, -58%); font-size: 58px; }
  .card-back .brand { left: 44px; top: 104px; font-size: 40px; }
  .card-back .brand-dot { width: 12px; height: 12px; }
  .contact {
    position: absolute; left: 330px; top: 102px; width: 210px;
    color: var(--text-white);
  }
  .contact-name { font-size: 15px; font-weight: 600; padding-bottom: 5px; white-space: nowrap; }
  .name-rule { height: 2px; background: var(--accent-red); margin-bottom: 8px; }
  .contact-address { font-size: 10px; font-weight: 500; line-height: 1.4; margin-bottom: 12px; white-space: nowrap; }
  .contact-row {
    display: flex; align-items: flex-start; gap: 8px;
    font-size: 10.5px; font-weight: 500; line-height: 1.45; margin-bottom: 8px;
    white-space: nowrap;
  }
  .contact-icon { width: 10px; flex: none; margin-top: 2px; }
</style>
</head>
<body>
<main class="canvas">

  <section class="card card-front" aria-label="Card front">
    <svg class="card-bg" viewBox="0 0 540 309" preserveAspectRatio="none" aria-hidden="true">
      <defs>
        <radialGradient id="frontGlow" cx="50%" cy="45%" r="65%">
          <stop offset="0" stop-color="var(--card-black-mid)"/>
          <stop offset="1" stop-color="var(--card-black)"/>
        </radialGradient>
      </defs>
      <rect width="540" height="309" fill="var(--swoosh-white)"/>
      <path d="M0 0 H250 C380 10 480 60 540 140 V309 H400 C300 260 140 215 0 205 Z" fill="url(#frontGlow)"/>
      <path d="M250 0 C380 10 480 60 540 140" fill="none" stroke="var(--accent-red)" stroke-width="2.5"/>
      <path d="M0 205 C140 215 300 260 400 309" fill="none" stroke="var(--accent-red)" stroke-width="2.5"/>
    </svg>
    <div class="brand"><span class="brand-dot"></span>BVEL7K</div>
  </section>

  <section class="card card-back" aria-label="Card back">
    <svg class="card-bg" viewBox="0 0 540 309" preserveAspectRatio="none" aria-hidden="true">
      <rect width="540" height="309" fill="var(--swoosh-white)"/>
      <path d="M0 0 H210 C340 5 470 40 540 90 V309 H420 C320 270 150 225 0 215 Z" fill="var(--card-black)"/>
      <path d="M210 0 C340 5 470 40 540 90" fill="none" stroke="var(--accent-red)" stroke-width="2.5"/>
      <path d="M0 215 C150 225 320 270 420 309" fill="none" stroke="var(--accent-red)" stroke-width="2.5"/>
    </svg>
    <div class="brand"><span class="brand-dot"></span>BVEL7K</div>

    <div class="contact">
      <p class="contact-name">Gordon Whitlock</p>
      <div class="name-rule"></div>
      <p class="contact-address">482 Tarrow Lane, Suite 207<br>Marlow Springs, GA 30412</p>
      <div class="contact-row">
        <svg class="contact-icon" viewBox="0 0 10 22" aria-hidden="true">
          <path d="M2 1 L4 1 L5 4 L3.5 5 Q4 7.5 5.5 9 L7 8 L9 10 L8 11.5 Q3 11 1.5 3 Z" fill="var(--accent-red)"/>
          <rect x="2" y="13" width="6" height="9" rx="1" fill="none" stroke="var(--accent-red)" stroke-width="1.3"/>
        </svg>
        <span>(770) 555-0142<br>(770) 555-0187</span>
      </div>
      <div class="contact-row">
        <svg class="contact-icon" viewBox="0 0 10 24" aria-hidden="true">
          <rect x="0.6" y="1" width="8.8" height="6" fill="none" stroke="var(--accent-red)" stroke-width="1.1"/>
          <path d="M0.6 1 L5 5 L9.4 1" fill="none" stroke="var(--accent-red)" stroke-width="1.1"/>
          <circle cx="5" cy="18" r="4.2" fill="none" stroke="var(--accent-red)" stroke-width="1.1"/>
          <path d="M0.8 18 H9.2 M5 13.8 V22.2" stroke="var(--accent-red)" stroke-width="0.9"/>
        </svg>
        <span>bvel7kga@quellmail.com<br>www.bvel7kga.com</span>
      </div>
    </div>
  </section>

</main>
</body>
</html>
```